Fenwick Nutrition Therapy needs a business card design

I need a business card design for my private practice. Green is my favorite color. I would like the back of the card to include an area for future appointment dates and time. I provide nutrition therapy to individuals, groups and families. I work a lot with adolescents and women who have eating disorders, but also work with athletes.
Updates

Reason: I received several new designs and would like to take some time reviewing them.

Target Market(s)

I am working primarily with women, but also men (mostly athletes). I work with a lot of runners. I work with people who are 14-60's.

Industry/Entity Type

Nutrition

Font styles to use
Serif
Sans Serif

Colors
9bcb3c
acd037

Requirements
Nice to have
• I would love to have 'Fenwick' incorporated into the design since it is my last name. If possible, I'd love to have an actual moon if it looks professional.

A picture of food could also be on the card if it is simple, but not sure how it would look with Fenwick. I am open to ideas for both Fenwick and a picture of a food item.

Other font style are fine as long as they are easy to read.

```html
<!DOCTYPE html>
<html lang="en">
<head>
<meta charset="utf-8">
<title>Fenwick Nutrition Therapy – Business Card Options</title>
<link rel="stylesheet" href="https://fonts.googleapis.com/css2?family=Raleway:wght@200;300;400&display=swap">
<style>
  :root{
    --green:#9bcb3c;
    --green-soft:#acd037;
    --lime:#d6df6a;
    --pale:#e8eaa0;
    --ink:#3a3a3a;
    --grey:#7a7a7a;
    --rule:#c9cbc6;
    --card:#eef0ee;
    --card-edge:#c8c8c8;
    --page:#ffffff;
  }
  *{box-sizing:border-box;margin:0;padding:0}
  html,body{width:891px;height:1200px;overflow:hidden;background:var(--page)}
  body{position:relative;font-family:"Raleway",sans-serif;color:var(--ink)}

  .option-label{position:absolute;left:24px;font-size:17px;font-weight:300;letter-spacing:1px;color:var(--ink)}

  /* wordmark */
  .brand{position:absolute;display:flex;align-items:center;gap:14px;z-index:2}
  .brand-dot{border-radius:50%;background:var(--green);flex:none}
  .brand-name{font-weight:300;color:var(--ink);white-space:nowrap;letter-spacing:1px}
  .brand--hero .brand-dot{width:104px;height:104px}
  .brand--hero .brand-name{font-size:40px}
  .brand--card .brand-dot{width:44px;height:44px}
  .brand--card .brand-name{font-size:20px}
  .brand--mini .brand-dot{width:26px;height:26px}
  .brand--mini .brand-name{font-size:15px}

  /* cards */
  .card{position:absolute;width:384px;height:216px;background:var(--card);border:1px solid var(--card-edge);box-shadow:inset 0 0 0 4px #f7f8f7;overflow:hidden}

  .holder{position:absolute;left:0;right:0;top:88px;text-align:center}
  .holder-name{display:inline-block;font-size:12px;font-weight:400;letter-spacing:1.5px;color:var(--grey);padding:0 20px 2px;border-bottom:1px solid var(--green)}
  .holder-title{font-size:7.5px;letter-spacing:1.5px;color:var(--grey);margin-top:3px}

  .contact{position:absolute;left:22px;top:136px;width:342px;font-size:11.5px;letter-spacing:1px;color:var(--green)}
  .contact-row{display:flex;border-top:1px solid var(--rule);height:17px;align-items:center}
  .contact-row:nth-child(2){border-bottom:1px solid var(--rule)}
  .contact-cell{width:120px;padding-right:4px;border-right:1px solid var(--rule);white-space:nowrap}
  .contact-cell + .contact-cell{width:auto;border-right:none;padding-left:6px}
  .contact-email{margin-top:6px;padding-top:2px;border-top:1px solid var(--rule);font-size:12px}
  .contact-email span{color:var(--grey)}

  /* appointment side */
  .appt-for{position:absolute;z-index:2;display:flex;align-items:flex-end;font-size:10px;letter-spacing:1px;color:var(--ink)}
  .appt-for::after{content:"";flex:1;border-bottom:1px solid var(--grey);margin-left:6px;height:1px}
  .slots{position:absolute;z-index:2;left:22px;top:70px;width:322px}
  .slot{display:flex;align-items:center;height:22px;font-size:10.5px;letter-spacing:1px;color:var(--green)}
  .slot-date,.slot-time{border-top:1px solid var(--rule);border-bottom:1px solid var(--rule);height:16px;line-height:15px;padding-left:2px}
  .slot-date{width:180px;border-right:1px solid var(--rule)}
  .slot-time{width:100px;margin-left:2px}
  .slot-ampm{margin-left:8px;display:grid;grid-template-columns:auto 8px;column-gap:3px;row-gap:1px;font-size:5.5px;color:var(--ink);line-height:7px}
  .slot-ampm i{display:block;width:8px;height:7px;border:1px solid var(--grey);background:#fff}
  .notice{position:absolute;z-index:2;left:20px;width:300px;text-align:center;font-size:8.5px;letter-spacing:.8px;line-height:11px;color:var(--grey);top:176px}
  .corner{position:absolute;z-index:1;right:0;bottom:0}
</style>
</head>
<body>

  <!-- Option 1 -->
  <div class="option-label" style="top:52px">OPTION 1</div>
  <div class="brand brand--hero" style="left:218px;top:110px">
    <span class="brand-dot"></span><span class="brand-name">FENWICK NUTRITION</span>
  </div>

  <section class="card" style="left:59px;top:304px" aria-label="Card front">
    <div class="brand brand--card" style="left:50px;top:20px;gap:12px">
      <span class="brand-dot"></span><span class="brand-name">FENWICK NUTRITION</span>
    </div>
    <div class="holder">
      <div class="holder-name">DANA ELLERY FENWICK</div>
      <div class="holder-title">NUTRITION THERAPY</div>
    </div>
    <div class="contact">
      <div class="contact-row"><span class="contact-cell">CELL:865.555.0148</span><span class="contact-cell">1406 WILLOW BEND ROAD</span></div>
      <div class="contact-row"><span class="contact-cell">FAX: 865.555.0172</span><span class="contact-cell">MARYVILLE, TN 37801</span></div>
      <div class="contact-email">EMAIL: <span>dfenwick@greenmail.net</span></div>
    </div>
  </section>

  <section class="card" style="left:472px;top:304px" aria-label="Card back">
    <span class="brand-dot" style="position:absolute;left:14px;top:12px;width:36px;height:36px"></span>
    <div class="appt-for" style="left:56px;top:20px;width:306px">APPOINTMENT FOR:</div>
    <div class="slots">
      <div class="slot"><span class="slot-date">DATE</span><span class="slot-time">At</span><span class="slot-ampm">AM<i></i>PM<i></i></span></div>
      <div class="slot"><span class="slot-date">DATE</span><span class="slot-time">At</span><span class="slot-ampm">AM<i></i>PM<i></i></span></div>
      <div class="slot"><span class="slot-date">DATE</span><span class="slot-time">At</span><span class="slot-ampm">AM<i></i>PM<i></i></span></div>
      <div class="slot"><span class="slot-date">DATE</span><span class="slot-time">At</span><span class="slot-ampm">AM<i></i>PM<i></i></span></div>
    </div>
    <p class="notice">IF UNABLE TO KEEP THIS APPOINTMENT<br>PLEASE GIVE 24 HOURS NOTICE</p>
    <svg class="corner" width="150" height="214" viewBox="0 0 150 214" role="img" aria-label="Faceted green and yellow corner decoration">
      <defs><linearGradient id="cornerFill1" x1="0" y1="1" x2="1" y2="0">
        <stop offset="0" stop-color="#9bcb3c"/><stop offset=".6" stop-color="#c7da6a"/><stop offset="1" stop-color="#e8eaa0"/>
      </linearGradient></defs>
      <polygon points="150,20 150,214 40,214 132,150" fill="url(#cornerFill1)"/>
    </svg>
  </section>

  <!-- Option 2 -->
  <div class="option-label" style="top:622px">OPTION 2</div>
  <div class="brand brand--hero" style="left:200px;top:666px">
    <span class="brand-dot"></span><span class="brand-name">FENWICK NUTRITION</span>
  </div>

  <section class="card" style="left:62px;top:888px" aria-label="Card front">
    <div class="brand brand--card" style="left:50px;top:20px;gap:12px">
      <span class="brand-dot"></span><span class="brand-name">FENWICK NUTRITION</span>
    </div>
    <div class="holder">
      <div class="holder-name">DANA ELLERY FENWICK</div>
      <div class="holder-title">NUTRITION THERAPY</div>
    </div>
    <div class="contact">
      <div class="contact-row"><span class="contact-cell">CELL:865.555.0148</span><span class="contact-cell">1406 WILLOW BEND ROAD</span></div>
      <div class="contact-row"><span class="contact-cell">FAX: 865.555.0172</span><span class="contact-cell">MARYVILLE, TN 37801</span></div>
      <div class="contact-email">EMAIL: <span>dfenwick@greenmail.net</span></div>
    </div>
  </section>

  <section class="card" style="left:469px;top:888px" aria-label="Card back">
    <div class="brand brand--mini" style="left:12px;top:10px;gap:6px">
      <span class="brand-dot"></span><span class="brand-name">FENWICK NUTRITION</span>
    </div>
    <div class="appt-for" style="left:74px;top:40px;width:270px">APPOINTMENT FOR:</div>
    <div class="slots" style="top:72px">
      <div class="slot"><span class="slot-date">DATE</span><span class="slot-time">At</span><span class="slot-ampm">AM<i></i>PM<i></i></span></div>
      <div class="slot"><span class="slot-date">DATE</span><span class="slot-time">At</span><span class="slot-ampm">AM<i></i>PM<i></i></span></div>
      <div class="slot"><span class="slot-date">DATE</span><span class="slot-time">At</span><span class="slot-ampm">AM<i></i>PM<i></i></span></div>
      <div class="slot"><span class="slot-date">DATE</span><span class="slot-time">At</span><span class="slot-ampm">AM<i></i>PM<i></i></span></div>
    </div>
    <p class="notice">IF UNABLE TO KEEP THIS APPOINTMENT<br>PLEASE GIVE 24 HOURS NOTICE</p>
    <svg class="corner" width="150" height="214" viewBox="0 0 150 214" role="img" aria-label="Faceted green and yellow corner decoration">
      <defs><linearGradient id="cornerFill2" x1="0" y1="1" x2="1" y2="0">
        <stop offset="0" stop-color="#9bcb3c"/><stop offset=".6" stop-color="#c7da6a"/><stop offset="1" stop-color="#e8eaa0"/>
      </linearGradient></defs>
      <polygon points="150,20 150,214 40,214 132,150" fill="url(#cornerFill2)"/>
    </svg>
  </section>

</body>
</html>
```